A empresa queria:
" O Grupo VELQUAR busca a conversão das mais inovadoras tecnologias nas soluções mais impactantes para o mercado. Nesta perspectiva, a VELQUAR BIOTECNOLOGIA ANIMAL constitui nosso segmento encarregado por transformar o conhecimento científico em bioferramentas inteligentes que agreguem o máximo valor às biotecnologias da reprodução tornando-as cada vez mais produtivas e lucrativas. Atuamos há mais de 10 anos no contexto da Reprodução Animal, dentro e fora do Brasil, executando tanto biotecnologias tradicionais, como a IATF (Inseminação Artificial em Tempo Fixo) e a SOV/TE (Superovulação e Transferência de Embriões), quanto bioferramentas modernas e de altíssimo impacto como a produção de embriões FIV (Fecundados In Vitro) e a clonagem animal. Nossa missão é contribuir decisivamente para o aprimoramento e emprego cada vez mais eficiente, rentável e satisfatório das biotecnologias da reprodução. Estruturado em valores como integridade, excelência e trabalho em equipe, constituímos uma companhia altamente amigável e absolutamente confiável para a execução das biotecnologias mais modernas com vistas, sempre, à plena satisfação do cliente. "

```html
<!DOCTYPE html>
<html lang="pt-BR">
<head>
<meta charset="utf-8">
<title>VELQUAR — A Empresa</title>
<link rel="stylesheet" href="https://fonts.googleapis.com/css2?family=Montserrat:wght@400;500;600;700&family=Open+Sans:wght@400;600&display=swap">
<style>
  :root {
    --green: #5aa137;
    --green-light: #7cc04a;
    --ink: #1d1d1b;
    --white: #ffffff;
    --stone: #bdb9b2;
    --stone-dark: #a9a59e;
    --text: #3a3a38;
    --hero-dark: #1f2a1c;
    --hero-mid: #3c4a30;
  }
  * { margin: 0; padding: 0; box-sizing: border-box; }
  html, body { width: 1200px; height: 1200px; overflow: hidden; background: var(--white); }
  .page { position: relative; width: 1200px; height: 1200px; overflow: hidden; font-family: "Open Sans", sans-serif; }

  .hero { position: absolute; inset: 0 0 auto 0; height: 560px; }
  .hero-photo { position: absolute; inset: 0;
    background: radial-gradient(ellipse at 70% 55%, var(--hero-mid) 0%, var(--hero-dark) 60%, #111810 100%); }
  .hero-shade { position: absolute; inset: 0; background: linear-gradient(90deg, rgba(0,0,0,.45) 0%, rgba(0,0,0,.15) 60%, rgba(0,0,0,.35) 100%); }

  .nav { position: absolute; top: 0; left: 0; right: 0; height: 100px; display: flex; align-items: center; padding: 0 120px 0 200px; }
  .brand { display: flex; align-items: center; gap: 12px; color: var(--green-light); font-family: "Montserrat", sans-serif; font-weight: 600; font-size: 30px; letter-spacing: 1px; }
  .brand-mark { width: 26px; height: 26px; border: 2px solid var(--green-light); }
  .menu { margin-left: auto; display: flex; align-items: center; gap: 48px; list-style: none;
    font-family: "Montserrat", sans-serif; font-weight: 600; font-size: 13px; letter-spacing: 1px; color: var(--white); }
  .menu .current { border: 1.5px solid var(--white); padding: 5px 10px; }
  .lang { display: flex; align-items: center; gap: 6px; font-size: 12px; }

  .hero-title { position: absolute; left: 200px; top: 240px; color: var(--white);
    font-family: "Montserrat", sans-serif; font-weight: 600; font-size: 58px; line-height: 1.2; }
  .scroll-down { position: absolute; left: 200px; top: 480px; }

  .about { position: absolute; top: 560px; left: 0; right: 0; bottom: 0; background: var(--stone); }
  .about-shapes { position: absolute; inset: 0; }
  .about-content { position: absolute; left: 200px; top: 100px; width: 520px; }
  .section-title { font-family: "Montserrat", sans-serif; font-weight: 600; font-size: 22px; letter-spacing: 2px; color: var(--text); }
  .section-title span { color: var(--green); }
  .subtitle { margin-top: 40px; font-family: "Montserrat", sans-serif; font-weight: 700; font-size: 14px; letter-spacing: 1px; color: var(--green); }
  .about-text { margin-top: 36px; font-size: 17px; line-height: 1.75; color: var(--text); }
</style>
</head>
<body>
<main class="page">
  <header class="hero">
    <div class="hero-photo" role="img" aria-label="Fotografia de gado bovino preto em pastagem"></div>
    <div class="hero-shade"></div>
    <nav class="nav">
      <div class="brand"><span class="brand-mark"></span>VELQUAR</div>
      <ul class="menu">
        <li>HOME</li>
        <li class="current">A EMPRESA</li>
        <li>SERVIÇOS</li>
        <li>FALE CONOSCO</li>
        <li class="lang">
          <svg width="12" height="12" viewBox="0 0 12 12"><circle cx="6" cy="6" r="5" fill="none" stroke="#fff" stroke-width="1.2"/><path d="M1 6h10M6 1c-2 3-2 7 0 10M6 1c2 3 2 7 0 10" fill="none" stroke="#fff" stroke-width=".8"/></svg>
          PT
        </li>
      </ul>
    </nav>
    <h1 class="hero-title">Conheça um<br>pouco mais<br>sobre nós</h1>
    <svg class="scroll-down" width="40" height="40" viewBox="0 0 40 40" aria-hidden="true">
      <circle cx="20" cy="20" r="18" fill="none" stroke="#fff" stroke-width="2.5"/>
      <path d="M20 11v17M13 21l7 7 7-7" fill="none" stroke="#fff" stroke-width="2.5" stroke-linecap="round" stroke-linejoin="round"/>
    </svg>
  </header>

  <section class="about">
    <svg class="about-shapes" width="1200" height="640" viewBox="0 0 1200 640" aria-hidden="true">
      <polygon points="0,0 150,0 0,120" fill="var(--stone-dark)"/>
      <polygon points="0,520 0,640 760,640" fill="var(--ink)"/>
      <polygon points="1200,190 1200,640 620,640" fill="var(--green)"/>
    </svg>
    <div class="about-content">
      <h2 class="section-title"><span>A</span> EMPRESA</h2>
      <h3 class="subtitle">MISSÃO E VALORES</h3>
      <p class="about-text">Nossa missão é contribuir decisivamente para o aprimoramento e emprego cada vez mais eficiente, rentável e satisfatório das biotecnologias da reprodução. Estruturado em valores como integridade, excelência e trabalho em equipe, constituímos uma companhia altamente amigável e absolutamente confiável para a execução das biotecnologias mais modernas com vistas, sempre, à plena satisfação do cliente.</p>
    </div>
  </section>
</main>
</body>
</html>
```